Tallbrook Meridian Advisory needs business cards

Tallbrook Meridian Advisory is a new approach to consulting: we believe in partnering our clients in a hands-on, side-by-side, rolling-up-our sleeves approach, rather than being removed and aloof consultants.

We have a logo design developped through PixelHarbor (see attachment) and need to move to the stage of designing a business card for our 7 founding members.

Target Market(s)

Senior executives in local and global companies (such as Fizzmont Tonic, Hollanby, Brevard, etc)

Industry/Entity Type

Business

Requirements
Must have
• Look and feel: The design reflect the logo: i.e. professional, modern and approachable (as opposed to corporate traditional and remote). We are looking for a high quality, premium design.

Content must haves:
- prominent: our logo, person's name, function, phone number and e-mail address
- less prominent: company address and website

Example: Tallbrook Meridian Advisory logo, Mireille Vostag, Partner, +44 (0)781 209 3375, mireille_vostag@tallbrookmeridian.example / 17 Pelham Crescent, Esher, Surrey, UK, KT10 3WN - www.tallbrookmeridian.example

- Both sides of the card can be used
- Both versions of the logo can be used (on black or on white)

```html
<!DOCTYPE html>
<html lang="en">
<head>
<meta charset="utf-8">
<title>Tallbrook Meridian Advisory – Business Cards</title>
<link rel="stylesheet" href="https://fonts.googleapis.com/css2?family=Arimo:wght@400;700&display=swap">
<style>
  :root {
    --page: #ffffff;
    --card-pale: #ebf4f8;
    --card-tint: #ddeef6;
    --band-blue: #74c3ea;
    --mark-blue: #1a9ad8;
    --ink: #2f2f2f;
    --ink-dark: #1e1e1e;
    --accent: #2a8fc8;
  }
  html, body {
    margin: 0;
    padding: 0;
    width: 1200px;
    height: 900px;
    overflow: hidden;
    background: var(--page);
    font-family: "Arimo", Arial, sans-serif;
  }
  .canvas {
    position: relative;
    width: 1200px;
    height: 900px;
  }
  .card {
    position: absolute;
    left: 331px;
    width: 538px;
    height: 347px;
    background: var(--card-pale);
    box-shadow: 0 18px 26px -14px rgba(0,0,0,0.28);
    overflow: hidden;
  }
  .card--front { top: 67px; }
  .card--back { top: 488px; }
  .card__art {
    position: absolute;
    inset: 0;
    width: 538px;
    height: 347px;
  }
  .brand {
    position: absolute;
    display: flex;
    align-items: center;
  }
  .brand__dot {
    border-radius: 50%;
    background: var(--mark-blue);
    flex: none;
  }
  .brand__name {
    color: var(--ink-dark);
    font-weight: 700;
    line-height: 1.05;
  }
  .card--front .brand { left: 21px; top: 95px; }
  .card--front .brand__dot { width: 146px; height: 146px; margin-right: 20px; }
  .card--front .brand__name { font-size: 33px; }
  .card--back .brand { left: 21px; top: 32px; }
  .card--back .brand__dot { width: 86px; height: 86px; margin-right: 12px; }
  .card--back .brand__name { font-size: 20px; }
  .person {
    position: absolute;
    left: 26px;
    top: 214px;
  }
  .person__name {
    margin: 0;
    font-size: 21px;
    font-weight: 400;
    color: var(--ink);
  }
  .person__role {
    margin: 2px 0 0;
    font-size: 16px;
    color: var(--accent);
  }
  .contact {
    position: absolute;
    left: 26px;
    top: 284px;
    margin: 0;
    font-size: 15.5px;
    line-height: 23px;
    color: var(--ink);
    font-style: normal;
  }
</style>
</head>
<body>
<div class="canvas">

  <section class="card card--front" aria-label="Card front">
    <svg class="card__art" viewBox="0 0 538 347" aria-hidden="true">
      <defs>
        <filter id="band-shadow" x="-10%" y="-20%" width="120%" height="160%">
          <feDropShadow dx="0" dy="4" stdDeviation="5" flood-color="#000" flood-opacity="0.28"/>
        </filter>
      </defs>
      <path d="M0,0 H538 V95 C430,48 220,26 0,28 Z" fill="var(--band-blue)" filter="url(#band-shadow)"/>
      <path d="M0,283 C150,308 350,318 538,312 V347 H0 Z" fill="var(--band-blue)"/>
    </svg>
    <div class="brand">
      <span class="brand__dot"></span>
      <span class="brand__name">Tallbrook Meridian<br>Advisory</span>
    </div>
  </section>

  <section class="card card--back" aria-label="Card back">
    <svg class="card__art" viewBox="0 0 538 347" aria-hidden="true">
      <path d="M0,0 H538 V202 C380,205 170,185 0,137 Z" fill="var(--card-tint)"/>
      <path d="M0,137 C170,185 380,205 538,202" fill="none" stroke="#c9dde6" stroke-width="1.5"/>
    </svg>
    <div class="brand">
      <span class="brand__dot"></span>
      <span class="brand__name">Tallbrook Meridian<br>Advisory</span>
    </div>
    <div class="person">
      <h2 class="person__name">Mireille Vostag</h2>
      <p class="person__role">Partner</p>
    </div>
    <address class="contact">
      +44 (0)781 209 3375<br>
      mireille_vostag@tallbrookmeridian.example
    </address>
  </section>

</div>
</body>
</html>
```